Leading equine advertising company needing three elements designed for an ad design

We have an advertisement design that we need assistance creating three elements (leather tags) that are cohesively designed and go with the overall advertisement design. Please see the highlighted areas.

Leather tags - I want to use complementary colors to 7c4627 for leather tags and use dark stitching. Colors need to be complementary to the leather dividers used in the footer. All three tag designs *MUST* be uniform; meaning - the same colors, same threads on leather stitching, texture/look and feel, etc. Leather tags must have a realistic look and text must be easy to see.

Top Leather Tag: Font: Use Font: Americane Condensed Weight: Bold
Bottom Leather Tags: Use Font: Play Weight: Bold

Please *ONLY* design the (3) elements (leather tags) that are highlighted in the reference picture.

See blank template to use for when you submit the design for leather tags, so we can see in real time how they would look on our current design.

Font styles to use
Sans Serif

Requirements
Must have
• Tags must all use the same colors, textures, and threading for leather. Want leather tags to have a realistic look to them. Please make sure text is easily to see on tags.

```html
<!DOCTYPE html>
<html lang="en">
<head>
<meta charset="utf-8">
<title>Broodmare Sale Ad</title>
<link rel="stylesheet" href="https://fonts.googleapis.com/css2?family=Oswald:wght@500;600;700&family=Roboto+Condensed:wght@700;800&family=Play:wght@400;700&display=swap">
<style>
  :root {
    --page: #a8a7a8;
    --paper: #ece2c8;
    --paper-edge: #d9ccab;
    --ink: #2b1a10;
    --accent: #c8763a;
    --leather: #7c4627;
    --leather-light: #a86a42;
    --leather-dark: #4e2a16;
    --stitch: #24130a;
    --wood: #2e1b12;
    --wood-dark: #1d110a;
    --cream: #f3ead8;
  }
  * { box-sizing: border-box; margin: 0; padding: 0; }
  html, body { width: 1200px; height: 1020px; overflow: hidden; background: var(--page); }
  .canvas { position: relative; width: 1200px; height: 1020px; }
  .ad {
    position: absolute; left: 185px; top: 95px;
    width: 908px; height: 908px;
    transform: scale(0.9141); transform-origin: 0 0;
    overflow: hidden; background: var(--wood);
    font-family: "Oswald", "Arial Narrow", sans-serif;
  }
  .defs { position: absolute; width: 0; height: 0; }
  .paper {
    position: absolute; left: 0; top: 0; width: 908px; height: 186px;
    background: linear-gradient(180deg, #efe6cf, var(--paper));
    z-index: 2;
  }
  .paper-edge { position: absolute; left: 0; top: 174px; z-index: 3; }
  .title { position: absolute; left: 14px; top: 10px; color: var(--ink); }
  .title h1 { font-family: "Roboto Condensed", "Arial Narrow", sans-serif; font-size: 31px; font-weight: 800; line-height: 1.15; }
  .title .breed { font-family: "Roboto Condensed", "Arial Narrow", sans-serif; font-size: 21px; font-weight: 700; color: var(--accent); line-height: 1.1; margin-bottom: 6px; }
  .title .lte { font-size: 14.5px; font-weight: 500; line-height: 21px; }

  .pedigree { position: absolute; inset: 0; color: var(--ink); font-weight: 500; }
  .pedigree span { position: absolute; white-space: nowrap; }
  .parent { font-size: 14px; text-align: right; right: 322px; line-height: 15.5px; }
  .grand { font-size: 13.5px; left: 603px; }
  .great { font-size: 11px; left: 766px; }
  .rule { position: absolute; height: 1.5px; background: var(--ink); }

  .photo {
    position: absolute; left: 76px; top: 180px; width: 756px; height: 526px;
    background: linear-gradient(180deg, #9cc2e6 0%, #c9dcec 18%, #6f8a5a 24%, #3e5a34 40%, #8f9f55 56%, #c2c07a 70%, #a9ab62 100%);
  }
  .photo-side {
    position: absolute; top: 180px; width: 76px; height: 526px;
    background: linear-gradient(180deg, #b9cfe6 0%, #8aa3ad 25%, #4f6340 45%, #a3a260 70%, #b9b676 100%);
    opacity: 0.9;
  }
  .photo-side.left { left: 0; }
  .photo-side.right { left: 832px; }

  .price-tag { position: absolute; left: 0; top: 128px; z-index: 4; width: 204px; height: 118px; }
  .price-tag svg { position: absolute; left: 0; top: 0; }
  .price-tag .price {
    position: absolute; left: 0; top: 0; width: 190px; height: 108px;
    display: flex; align-items: center; justify-content: center;
    font-size: 44px; font-weight: 700; color: var(--cream); letter-spacing: -0.5px;
    text-shadow: -1.5px -1.5px 0 var(--stitch), 1.5px -1.5px 0 var(--stitch), -1.5px 1.5px 0 var(--stitch), 1.5px 1.5px 0 var(--stitch), 0 3px 4px rgba(0,0,0,.6);
  }

  .leather-band { position: absolute; left: 0; top: 698px; z-index: 4; }
  .tag-label {
    position: absolute; top: 732px; z-index: 5;
    font-family: "Play", sans-serif; font-weight: 700; font-size: 17px; color: var(--ink);
    text-shadow: 0 1px 0 rgba(255,220,180,.35);
  }
  .tag-label.left { left: 24px; }
  .tag-label.right { left: 748px; }
  .disciplines {
    position: absolute; top: 746px; left: 0; width: 908px; text-align: center; z-index: 5;
    font-family: "Play", sans-serif; font-weight: 700; font-size: 11px; color: var(--cream); letter-spacing: 0.3px;
  }

  .footer {
    position: absolute; left: 0; top: 770px; width: 908px; height: 110px;
    background: linear-gradient(180deg, #3a2418, var(--wood) 40%, #24150d);
    font-family: "Play", sans-serif; color: var(--cream); text-align: center;
  }
  .brand { position: absolute; left: 42px; top: 28px; text-align: left; white-space: nowrap; }
  .brand-name { display: flex; align-items: center; gap: 8px; font-weight: 700; font-size: 28px; line-height: 1; color: var(--cream); }
  .brand-name i { width: 18px; height: 18px; border-radius: 50%; background: var(--cream); display: block; }
  .brand-url { font-size: 11.5px; font-weight: 700; margin-top: 8px; letter-spacing: 0.2px; }
  .contact { position: absolute; left: 313px; width: 280px; top: 14px; }
  .location { position: absolute; left: 616px; width: 280px; top: 20px; }
  .heading { font-size: 21px; font-weight: 700; letter-spacing: 1px; line-height: 1.1; }
  .highlight { font-size: 16.5px; font-weight: 700; color: var(--accent); line-height: 1.3; }
  .detail { font-size: 14.5px; line-height: 23px; }
  .location .detail { font-weight: 700; font-size: 14px; line-height: 20px; }

  .legal {
    position: absolute; left: 0; top: 880px; width: 908px; height: 28px;
    background: var(--wood-dark); border-top: 2px solid var(--leather);
    color: var(--cream); font-family: "Play", sans-serif; font-weight: 700;
  }
  .legal .listing { position: absolute; left: 12px; top: 5px; font-size: 12px; }
  .legal .copyright { position: absolute; left: 74px; top: 8px; font-size: 8px; }
  .legal .notice {
    position: absolute; right: 8px; top: 7px; font-size: 7.5px; padding: 0 2px;
    border: 1px solid var(--cream); line-height: 9px;
  }
</style>
</head>
<body>
<div class="canvas">
  <div class="ad">
    <svg class="defs" width="0" height="0" aria-hidden="true">
      <defs>
        <filter id="leatherGrain" x="0" y="0" width="100%" height="100%" color-interpolation-filters="sRGB">
          <feTurbulence type="fractalNoise" baseFrequency="0.75" numOctaves="3" seed="7" result="fine"/>
          <feDiffuseLighting in="fine" surfaceScale="1.8" lighting-color="#ffffff" result="pebble">
            <feDistantLight azimuth="225" elevation="60"/>
          </feDiffuseLighting>
          <feTurbulence type="fractalNoise" baseFrequency="0.018" numOctaves="2" seed="3" result="mottle"/>
          <feColorMatrix in="mottle" type="matrix" values="0 0 0 0 0  0 0 0 0 0  0 0 0 0 0  0 0 0 0.55 -0.12" result="mottleShade"/>
          <feBlend in="SourceGraphic" in2="pebble" mode="multiply" result="grained"/>
          <feComposite in="mottleShade" in2="grained" operator="over" result="shaded"/>
          <feComposite in="shaded" in2="SourceAlpha" operator="in"/>
        </filter>
        <filter id="tagShadow" x="-10%" y="-10%" width="125%" height="135%">
          <feDropShadow dx="1.5" dy="3" stdDeviation="2.5" flood-color="#000" flood-opacity="0.55"/>
        </filter>
        <linearGradient id="leatherTag" x1="0" y1="0" x2="0" y2="1">
          <stop offset="0" stop-color="#c0825a"/>
          <stop offset="0.45" stop-color="#a86a42"/>
          <stop offset="1" stop-color="#7c4627"/>
        </linearGradient>
        <linearGradient id="leatherPrice" x1="0" y1="0" x2="0" y2="1">
          <stop offset="0" stop-color="#a7673f"/>
          <stop offset="0.5" stop-color="#7c4627"/>
          <stop offset="1" stop-color="#5c311a"/>
        </linearGradient>
        <linearGradient id="leatherStrap" x1="0" y1="0" x2="0" y2="1">
          <stop offset="0" stop-color="#5a311c"/>
          <stop offset="0.5" stop-color="#40210f"/>
          <stop offset="1" stop-color="#2c160a"/>
        </linearGradient>
        <radialGradient id="sheen" cx="0.35" cy="0.25" r="0.8">
          <stop offset="0" stop-color="#fff" stop-opacity="0.22"/>
          <stop offset="1" stop-color="#fff" stop-opacity="0"/>
        </radialGradient>
      </defs>
    </svg>

    <div class="photo-side left" role="img" aria-label="Soft blurred extension of the pasture scene"></div>
    <div class="photo" role="img" aria-label="Photo of a bay broodmare standing in a grassy pasture with trees and sky behind"></div>
    <div class="photo-side right" role="img" aria-label="Soft blurred extension of the pasture scene"></div>

    <div class="paper">
      <div class="title">
        <h1>REGISTERED NAME</h1>
        <div class="breed">2020 SORREL BROODMARE</div>
        <div class="lte">LTE $XX,XXX</div>
        <div class="lte">LTE $XX,XXX</div>
      </div>

      <div class="pedigree">
        <span class="parent" style="top:40px">SIRE<br>LTE $XX,XXX<br>LTE $XX,XXX</span>
        <span class="parent" style="top:114px">DAM<br>LTE $XX,XXX<br>LTE $XX,XXX</span>

        <span class="grand" style="top:28px">SIRE'S SIRE</span>
        <div class="rule" style="left:600px; top:47px; width:150px"></div>
        <span class="grand" style="top:51px">SIRE'S DAM</span>
        <span class="grand" style="top:103px">DAM'S SIRE</span>
        <div class="rule" style="left:600px; top:122px; width:150px"></div>
        <span class="grand" style="top:126px">DAM'S DAM</span>

        <span class="great" style="top:15px">SIRE'S SIRE'S SIRE</span>
        <div class="rule" style="left:763px; top:30px; width:128px"></div>
        <span class="great" style="top:33px">SIRE'S SIRE'S DAM</span>
        <span class="great" style="top:51px">SIRE'S DAM'S SIRE</span>
        <div class="rule" style="left:763px; top:66px; width:128px"></div>
        <span class="great" style="top:69px">SIRE'S DAM'S DAM</span>
        <span class="great" style="top:90px">DAM'S SIRE'S SIRE</span>
        <div class="rule" style="left:763px; top:104px; width:128px"></div>
        <span class="great" style="top:107px">DAM'S SIRE'S DAM</span>
        <span class="great" style="top:125px">DAM'S DAM'S SIRE</span>
        <div class="rule" style="left:763px; top:140px; width:128px"></div>
        <span class="great" style="top:142px">DAM'S DAM'S DAM</span>
      </div>
    </div>
    <svg class="paper-edge" width="908" height="14" viewBox="0 0 908 14" aria-hidden="true">
      <path d="M0 0 H908 V6 L880 9 L850 5 L820 10 L790 6 L760 9 L730 5 L700 10 L670 6 L640 9 L610 5 L580 10 L550 6 L520 9 L490 5 L460 10 L430 6 L400 9 L370 5 L340 10 L310 6 L280 9 L250 5 L220 10 L190 6 L160 9 L130 5 L100 10 L70 6 L40 9 L10 5 L0 7 Z" fill="var(--paper-edge)"/>
      <path d="M0 0 H908 V3 L880 6 L850 2 L820 7 L790 3 L760 6 L730 2 L700 7 L670 3 L640 6 L610 2 L580 7 L550 3 L520 6 L490 2 L460 7 L430 3 L400 6 L370 2 L340 7 L310 3 L280 6 L250 2 L220 7 L190 3 L160 6 L130 2 L100 7 L70 3 L40 6 L10 2 L0 4 Z" fill="var(--paper)"/>
    </svg>

    <div class="price-tag">
      <svg width="204" height="118" viewBox="0 0 204 118" aria-hidden="true">
        <g filter="url(#tagShadow)">
          <path d="M0 0 H178 Q192 0 192 14 V94 Q192 108 178 108 H0 Z" fill="url(#leatherPrice)" filter="url(#leatherGrain)"/>
        </g>
        <path d="M0 0 H178 Q192 0 192 14 V94 Q192 108 178 108 H0 Z" fill="url(#sheen)"/>
        <path d="M0 1.5 H178 Q190.5 1.5 190.5 14 V94 Q190.5 106.5 178 106.5 H0" fill="none" stroke="var(--leather-dark)" stroke-width="3"/>
        <path d="M0 4.5 H177 Q187.5 4.5 187.5 15" fill="none" stroke="#d49a70" stroke-opacity="0.45" stroke-width="1"/>
        <path d="M0 10 H175 Q182 10 182 17 V91 Q182 98 175 98 H0" fill="none" stroke="#c68a60" stroke-opacity="0.5" stroke-width="1.2" transform="translate(0 1)"/>
        <path d="M0 10 H175 Q182 10 182 17 V91 Q182 98 175 98 H0" fill="none" stroke="#3a1d0e" stroke-opacity="0.5" stroke-width="2.6"/>
        <path d="M0 10 H175 Q182 10 182 17 V91 Q182 98 175 98 H0" fill="none" stroke="var(--stitch)" stroke-width="1.8" stroke-linecap="round" stroke-dasharray="4 3.5"/>
      </svg>
      <div class="price">$300,000</div>
    </div>

    <svg class="leather-band" width="908" height="72" viewBox="0 0 908 72" aria-hidden="true">
      <g filter="url(#tagShadow)">
        <rect x="0" y="32" width="908" height="40" fill="url(#leatherStrap)" filter="url(#leatherGrain)"/>
      </g>
      <path d="M0 33 H908" stroke="#6e3d22" stroke-width="1.5"/>
      <path d="M0 39 H908 M0 65 H908" stroke="#8a5634" stroke-opacity="0.55" stroke-width="1" transform="translate(0 1)"/>
      <path d="M0 39 H908 M0 65 H908" stroke="#a86a42" stroke-width="1.5" stroke-linecap="round" stroke-dasharray="4 3.5"/>
      <rect x="0" y="69" width="908" height="3" fill="var(--leather)"/>

      <g filter="url(#tagShadow)">
        <path d="M0 4 H186 Q198 4 204 15 L227 72 H0 Z" fill="url(#leatherTag)" filter="url(#leatherGrain)"/>
      </g>
      <path d="M0 4 H186 Q198 4 204 15 L227 72 H0 Z" fill="url(#sheen)"/>
      <path d="M0 5.5 H186 Q197 5.5 202.5 15.5 L225 72" fill="none" stroke="var(--leather-dark)" stroke-width="3"/>
      <path d="M0 11 H182 Q192 11 197 20 L217 70" fill="none" stroke="#3a1d0e" stroke-opacity="0.5" stroke-width="2.6"/>
      <path d="M0 12 H182 Q192 12 197 21 L217 71" fill="none" stroke="#dba27a" stroke-opacity="0.45" stroke-width="1"/>
      <path d="M0 11 H182 Q192 11 197 20 L217 70" fill="none" stroke="var(--stitch)" stroke-width="1.8" stroke-linecap="round" stroke-dasharray="4 3.5"/>

      <g filter="url(#tagShadow)">
        <path d="M908 4 H722 Q710 4 704 15 L681 72 H908 Z" fill="url(#leatherTag)" filter="url(#leatherGrain)"/>
      </g>
      <path d="M908 4 H722 Q710 4 704 15 L681 72 H908 Z" fill="url(#sheen)"/>
      <path d="M908 5.5 H722 Q711 5.5 705.5 15.5 L683 72" fill="none" stroke="var(--leather-dark)" stroke-width="3"/>
      <path d="M908 11 H726 Q716 11 711 20 L691 70" fill="none" stroke="#3a1d0e" stroke-opacity="0.5" stroke-width="2.6"/>
      <path d="M908 12 H726 Q716 12 711 21 L691 71" fill="none" stroke="#dba27a" stroke-opacity="0.45" stroke-width="1"/>
      <path d="M908 11 H726 Q716 11 711 20 L691 70" fill="none" stroke="var(--stitch)" stroke-width="1.8" stroke-linecap="round" stroke-dasharray="4 3.5"/>
    </svg>
    <div class="tag-label left">FOAL INCENTIVES</div>
    <div class="tag-label right">DAM PICTURED</div>
    <div class="disciplines">DISCIPLINES: DISCIPLINE 1, DISCIPLINE 2, DISCIPLINE 3</div>

    <div class="footer">
      <div class="brand">
        <div class="brand-name"><i></i>SUMMIT STABLE</div>
        <div class="brand-url">WWW.SUMMITSTABLE.COM</div>
      </div>
      <div class="contact">
        <div class="heading">CONTACT</div>
        <div class="highlight">FIRST NAME LAST NAME</div>
        <div class="detail">(000) 000-0000</div>
        <div class="detail">EMAIL@EMAIL.COM</div>
      </div>
      <div class="location">
        <div class="heading">LOCATION</div>
        <div class="highlight">CITY, STATE</div>
        <div class="detail">TRANSPORT: BUYERS EXPENSE</div>
      </div>
    </div>

    <div class="legal">
      <span class="listing">L#00000</span>
      <span class="copyright">COPYRIGHT © SUMMIT STABLE, LLC.</span>
      <span class="notice">DO NOT ALTER</span>
    </div>
  </div>
</div>
</body>
</html>
```